QuillHarbor New Website

QuillHarbor is a digital marketing agency. Our clients are all limousine companies. We need a responsive website designed to highlight our services and products. Our competition is http://www.velmorastudiohub.com/ and we need a site of similar design and layout without being too similar. Our old website www.quillharbor.com, is very outdated and the logo and graphics have changed. We will adjust the content to work with the new design. The new logo is attached.

Industry/Entity Type

Digital

Coding

Coded - Design and coding required

```html
<!DOCTYPE html>
<html lang="en">
<head>
<meta charset="utf-8">
<title>QuillHarbor — Brand Savvy. Industry Smart.</title>
<link rel="stylesheet" href="https://fonts.googleapis.com/css2?family=Open+Sans:wght@300;400;600;700;800&display=swap">
<style>
:root{
  --navy:#4b5876;
  --slate:#5a6787;
  --slate-light:#6c7898;
  --nav:#5b6886;
  --nav-active:#6d7a98;
  --gold:#a08a1c;
  --gold-dark:#8c7816;
  --footer:#3c4560;
  --footer-bottom:#343c55;
  --card:#3f4863;
  --text:#6d6d6d;
  --light-bg:#f4f4f4;
  --white:#ffffff;
}
*{box-sizing:border-box;margin:0;padding:0}
html,body{width:1200px;height:2731px;overflow:hidden}
body{font-family:"Open Sans",Arial,sans-serif;color:var(--text);background:var(--white);position:relative}
section,header,nav,footer{position:absolute;left:0;width:1200px}
.abs{position:absolute}

/* header */
.site-header{top:0;height:133px;background:var(--light-bg);text-align:center}
.brand{position:absolute;top:8px;left:0;width:100%;font-size:52px;font-weight:300;color:var(--navy);letter-spacing:-1px;line-height:60px}
.tagline{position:absolute;top:70px;left:0;width:100%;font-size:10px;font-weight:700;color:var(--navy);letter-spacing:.5px}
.contact-line{position:absolute;top:96px;left:0;width:100%;font-size:14px;color:var(--navy);display:flex;justify-content:center;gap:22px;align-items:center}
.contact-line span{display:flex;align-items:center;gap:8px}

/* nav */
.main-nav{top:133px;height:42px;background:var(--nav)}
.main-nav ul{list-style:none;display:flex;justify-content:center;height:42px}
.main-nav li{color:var(--white);font-size:13px;line-height:42px;padding:0 21px}
.main-nav li.active{background:var(--nav-active)}

/* hero */
.hero{top:175px;height:395px;background:linear-gradient(90deg,#e6e7ea 0%,#f3f3f4 60%,#f7f7f7 100%)}
.hero-photo{left:0;top:0;width:640px;height:395px;background:linear-gradient(90deg,#5a5f68 0%,#8a8d93 30%,#b9bbc0 65%,rgba(243,243,244,0) 100%)}
.hero-title{left:648px;top:94px;font-size:29px;color:var(--navy);font-weight:400}
.hero-sub{left:648px;top:128px;font-size:19px;color:var(--gold);font-weight:600}
.hero-text{left:648px;top:166px;width:445px;font-size:13px;line-height:21px;color:#8a8a8a}
.btn{display:inline-block;background:var(--gold);color:var(--white);text-align:center;font-size:13px;text-transform:uppercase}
.hero .btn{position:absolute;left:648px;top:244px;width:168px;height:44px;line-height:44px;font-size:14px}

/* welcome */
.welcome{top:570px;height:395px;background:var(--white)}
.section-title{position:absolute;left:0;width:100%;text-align:center;font-weight:800;font-size:34px;color:var(--navy);text-transform:uppercase}
.section-sub{position:absolute;left:0;width:100%;text-align:center;font-size:14px;color:#8a8a8a}
.welcome .section-title{top:30px}
.welcome .section-sub{top:78px}
.welcome-copy{left:120px;top:134px;width:526px;font-size:12px;line-height:22px;color:#7a7a7a}
.welcome-copy p+p{margin-top:18px}
.team-photo{left:683px;top:82px;width:410px;height:313px;background:radial-gradient(ellipse at 50% 45%,#c9c3bb 0%,#a6a4a6 45%,rgba(255,255,255,0) 75%)}
.help-box{left:747px;top:244px;width:273px;height:118px;background:var(--gold);color:var(--white);text-align:center;padding-top:12px}
.help-box h3{font-size:16px;font-weight:700}
.help-box p{font-size:11px;line-height:17px;margin:8px 24px 0}
.help-box strong{display:block;font-size:20px;font-weight:600;margin-top:10px}

/* features */
.features{top:965px;height:474px;background:var(--slate)}
.features-photo{left:0;top:0;width:440px;height:474px;background:linear-gradient(90deg,#2f3446 0%,#6a6f7e 35%,#9aa0b0 60%,rgba(90,103,135,0) 100%)}
.features .section-title{left:320px;width:740px;top:38px;color:var(--white)}
.features .section-sub{left:320px;width:740px;top:82px;color:var(--white);font-size:14px}
.accordion{left:499px;top:126px;width:492px}
.acc-head{height:40px;margin-bottom:8px;background:var(--slate-light);color:var(--white);font-size:12px;font-weight:600;text-transform:uppercase;line-height:40px;padding-left:16px;position:relative}
.acc-head.open{background:var(--gold);margin-bottom:0}
.acc-head::after{content:"+";position:absolute;right:14px;top:0;font-size:28px;font-weight:300}
.acc-head.open::after{content:"–"}
.acc-body{color:#e4e7ef;font-size:11.5px;line-height:20px;padding:12px 0 14px}
.acc-body b{color:var(--white);display:block;margin-top:2px}

/* services */
.services{top:1439px;height:464px;background:var(--white)}
.services .section-title{top:30px}
.services .section-sub{top:86px}
.service{top:136px;width:220px;text-align:center}
.service svg{display:block;margin:0 auto;width:92px;height:92px}
.service h4{margin-top:20px;font-size:17px;font-weight:400;color:#4a4a4a}
.service p{margin-top:10px;font-size:11.5px;line-height:18.5px;color:#6d6d6d;padding:0 8px}
.service .btn{margin-top:22px;width:124px;height:36px;line-height:36px}
.arrow{top:248px}

/* testimonials */
.testimonials{top:1903px;height:321px;background:var(--slate)}
.testimonials .section-title{top:36px;color:var(--white)}
.rating{left:0;width:100%;top:84px;text-align:center;color:var(--white);font-size:12px;font-weight:700;display:flex;justify-content:center;align-items:center;gap:4px}
.quote{top:137px;width:397px;height:133px;background:var(--card);padding:22px 20px 0 124px;color:var(--white)}
.avatar{position:absolute;left:16px;top:20px;width:92px;height:92px;border-radius:50%;border:3px solid #9fa7bb;background:radial-gradient(circle at 50% 40%,#c9b6a3 0%,#7e8aa3 70%)}
.quote p{font-size:12.5px;line-height:19px;font-weight:600}
.quote cite{display:block;margin-top:10px;font-size:10px;font-style:normal;color:#b9c0d0}

/* footer */
.site-footer{top:2224px;height:438px;background:var(--footer);color:#c8cdd9}
.footer-heading{position:absolute;top:42px;color:var(--white);font-size:19px;font-weight:700;text-transform:uppercase}
.link-col{top:88px;width:215px;list-style:none}
.link-col li{font-size:13.5px;line-height:20px;padding:8px 0 10px;border-bottom:1px solid #4a5370}
.link-col li:last-child{border-bottom:none}
.follow{left:120px;top:338px;width:328px;height:52px;background:#343c55;display:flex;align-items:center;padding-left:24px;gap:14px;font-size:13px;color:#c8cdd9}
.follow i{display:inline-block;width:18px;height:18px;border-radius:50%;background:var(--white)}
.post{left:710px;width:370px;height:104px;border-bottom:1px solid #4a5370}
.date{position:absolute;left:0;top:0;width:44px;height:44px;background:#4a5370;text-align:center;color:var(--white);font-size:8px;line-height:12px;padding-top:4px}
.date b{display:block;font-size:20px;font-weight:700;line-height:22px}
.post p{position:absolute;left:62px;top:-2px;font-size:14px;line-height:25px;color:#c8cdd9}
.post a{position:absolute;left:62px;top:56px;font-size:14px;color:var(--white);text-decoration:none}
.footer-bottom{top:2662px;height:69px;background:var(--footer-bottom);color:#c8cdd9;font-size:10px;text-transform:uppercase}
.legal{left:120px;top:28px;word-spacing:2px}
.copyright{right:120px;top:28px}
</style>
</head>
<body>

<header class="site-header">
  <div class="brand">quillharbor</div>
  <div class="tagline">BRAND SAVVY. INDUSTRY SMART.</div>
  <div class="contact-line">
    <span><svg width="13" height="13" viewBox="0 0 24 24"><path fill="#4b5876" d="M6.6 10.8a15.1 15.1 0 0 0 6.6 6.6l2.2-2.2a1 1 0 0 1 1-.25 11.4 11.4 0 0 0 3.6.57 1 1 0 0 1 1 1V20a1 1 0 0 1-1 1A17 17 0 0 1 3 4a1 1 0 0 1 1-1h3.5a1 1 0 0 1 1 1c0 1.25.2 2.45.57 3.57a1 1 0 0 1-.25 1z"/></svg>855-730-4418</span>
    <span><svg width="14" height="11" viewBox="0 0 24 18"><rect x="1" y="1" width="22" height="16" fill="#4b5876"/><path d="M1 1l11 9 11-9" fill="none" stroke="#f4f4f4" stroke-width="2"/></svg>info@quillharbor.com</span>
  </div>
</header>

<nav class="main-nav">
  <ul>
    <li class="active">Home</li><li>About Us</li><li>Integrated Marketing</li><li>Services</li><li>News &amp; Events</li><li>RideKeep™</li><li>Blog</li><li>Contact Us</li>
  </ul>
</nav>

<section class="hero">
  <div class="abs hero-photo" role="img" aria-label="Photo of a smiling team of five business professionals in suits"></div>
  <h1 class="abs hero-title">We Have A Passion</h1>
  <h2 class="abs hero-sub">For What We Do. Let Us Do What We Do Best ...</h2>
  <p class="abs hero-text">Lorem ipsum dolor sit amet, consectetur adipiscing elit. Nulla porta erat at sodales ultricies. Nullam est odio, finibus a ullamcorper eu, rhoncus ac purus.</p>
  <a class="btn">Find Out More</a>
</section>

<section class="welcome">
  <h2 class="section-title">Welcome to QuillHarbor</h2>
  <p class="section-sub">Helping Businesses THRIVE by turning every transaction into a relationship.</p>
  <div class="abs welcome-copy">
    <p>Lorem ipsum dolor sit amet, consectetur adipiscing elit. In laoreet justo tincidunt molestie viverra. Suspendisse malesuada nisl eget tempus eleifend. Pellentesque sodales eros nec sem lobortis, ut viverra dolor rhoncus. Cras rhoncus justo nec urna aliquet sodales. Praesent lacinia sed augue id venenatis. Donec molestie mattis neque, sed tempor purus. Mauris dignissim commodo pretium. Curabitur vehicula rhoncus felis consectetur rutrum.</p>
    <p>Aliquam in dolor sollicitudin, ornare tortor et, convallis justo. Ut velit erat, dictum ut maximus vel, faucibus in dolor. Quisque lacinia ex nec placerat ultricies. Vestibulum leo augue, tempus id mi in, congue faucibus nibh. Aliquam fermentum lectus sed finibus finibus. Fusce sit amet velit ut sapien faucibus scelerisque. Maecenas eget nulla est.</p>
  </div>
  <div class="abs team-photo" role="img" aria-label="Photo of four smiling support team members"></div>
  <div class="abs help-box">
    <h3>Need Help?</h3>
    <p>Call one of our experts. That can be on week days from 9.00-17.00!</p>
    <strong>855-730-4418</strong>
  </div>
</section>

<section class="features">
  <div class="abs features-photo" role="img" aria-label="Photo of a smiling woman in a light blue shirt"></div>
  <h2 class="section-title">Some Key Features</h2>
  <p class="section-sub">We Have A Passion For What We Do. Let Us Do What We Do Best ... QuillHarbor.</p>
  <div class="abs accordion">
    <div class="acc-head open">We're not just raising the stakes. We're changing the game.</div>
    <div class="acc-body">Lorem ipsum dolor sit amet, consectetur adipiscing elit. Nulla porta erat at sodales ultricies. Nullam est odio, finibus a ullamcorper eu, rhoncus ac purus. Sed erat sem, pretium sit amet fringilla et, elementum at arcu. Fusce iaculis tincidunt faucibus. Cras vel ipsum in augue maximus lacinia et nec dui. In hac habitasse platea dictumst. Sed iaculis luctus erat in congue.<b>read more...</b></div>
    <div class="acc-head">Limousine Industry Specialists</div>
    <div class="acc-head">Your Marketing Message Matters</div>
    <div class="acc-head">You're in the Experience Business</div>
  </div>
</section>

<section class="services">
  <h2 class="section-title">Our Services</h2>
  <p class="section-sub">We're providing some helpful service that can grow your business</p>

  <svg class="abs arrow" style="left:76px" width="30" height="54" viewBox="0 0 30 54"><path d="M27 2L3 27l24 25" fill="none" stroke="#c8c8c8" stroke-width="2"/></svg>
  <svg class="abs arrow" style="left:1094px" width="30" height="54" viewBox="0 0 30 54"><path d="M3 2l24 25L3 52" fill="none" stroke="#c8c8c8" stroke-width="2"/></svg>

  <div class="abs service" style="left:114px">
    <svg viewBox="0 0 92 92"><g fill="none" stroke="#a08a1c" stroke-width="9" stroke-linecap="round"><path d="M40 52l-12 12a9 9 0 0 1-13-13l12-12"/><path d="M42 38l10-10a9 9 0 0 1 13 13L55 51"/><path d="M36 56l20-20"/></g><circle cx="70" cy="20" r="16" fill="#a08a1c"/><path d="M70 11v18M61 20h18" stroke="#fff" stroke-width="4"/></svg>
    <h4>InBound Marketing</h4>
    <p>Fusce volutpat suscipit semper. Nunc aliquet elit quis ex semper, sit amet convallis ligula porttitor. Morbi a sapien vitae dolor lobortis efficitur.</p>
    <a class="btn">Read More</a>
  </div>
  <div class="abs service" style="left:369px">
    <svg viewBox="0 0 92 92"><path fill="#a08a1c" d="M78 14c-18 0-32 8-42 24l-12 2-10 12 14 2 18 18 2 14 12-10 2-12c16-10 24-24 24-42zM60 26a6 6 0 1 1 0 12 6 6 0 0 1 0-12zM22 60l10 10-16 10z"/></svg>
    <h4>OutBound Marketing</h4>
    <p>Fusce volutpat suscipit semper. Nunc aliquet elit quis ex semper, sit amet convallis ligula porttitor. Morbi a sapien vitae dolor lobortis efficitur.</p>
    <a class="btn">Read More</a>
  </div>
  <div class="abs service" style="left:620px">
    <svg viewBox="0 0 92 92"><g fill="#a08a1c"><circle cx="24" cy="46" r="12"/><circle cx="66" cy="22" r="12"/><circle cx="66" cy="70" r="12"/></g><path d="M24 46L66 22M24 46l42 24" stroke="#a08a1c" stroke-width="6"/></svg>
    <h4>Social Media Marketing</h4>
    <p>Fusce volutpat suscipit semper. Nunc aliquet elit quis ex semper, sit amet convallis ligula porttitor. Morbi a sapien vitae dolor lobortis efficitur.</p>
    <a class="btn">Read More</a>
  </div>
  <div class="abs service" style="left:868px">
    <svg viewBox="0 0 92 92"><rect x="26" y="6" width="40" height="80" rx="8" fill="#a08a1c"/><rect x="32" y="18" width="28" height="52" fill="#fff"/><circle cx="46" cy="78" r="4" fill="#fff"/></svg>
    <h4>Mobile Marketing</h4>
    <p>Fusce volutpat suscipit semper. Nunc aliquet elit quis ex semper, sit amet convallis ligula porttitor. Morbi a sapien vitae dolor lobortis efficitur.</p>
    <a class="btn">Read More</a>
  </div>
</section>

<section class="testimonials">
  <h2 class="section-title">What Our Client Says</h2>
  <div class="abs rating">
    <svg width="90" height="16" viewBox="0 0 90 16"><g fill="#fff"><path id="star" d="M8 0l2.4 5 5.6.6-4.2 3.8 1.2 5.6L8 12.2 3 15l1.2-5.6L0 5.6 5.6 5z"/><use href="#star" x="18"/><use href="#star" x="36"/><use href="#star" x="54"/><use href="#star" x="72"/></g></svg>
    <span>&nbsp;5.0</span>
  </div>
  <svg class="abs" style="left:118px;top:134px" width="30" height="54" viewBox="0 0 30 54"><path d="M27 2L3 27l24 25" fill="none" stroke="#8a94ae" stroke-width="2"/></svg>
  <svg class="abs" style="left:1050px;top:134px" width="30" height="54" viewBox="0 0 30 54"><path d="M3 2l24 25L3 52" fill="none" stroke="#8a94ae" stroke-width="2"/></svg>
  <div class="abs quote" style="left:188px">
    <div class="avatar" role="img" aria-label="Portrait photo of the client"></div>
    <p>“Fusce volutpat suscipit semper. Nunc aliquet elit quis ex semper, sit amet convallis ligula porttitor. Morbi a sapien vitae dolor lobortis efficitur.</p>
    <cite>Alex Marlow – A Lorem Ipsum Co.</cite>
  </div>
  <div class="abs quote" style="left:614px">
    <div class="avatar" role="img" aria-label="Portrait photo of the client"></div>
    <p>“Fusce volutpat suscipit semper. Nunc aliquet elit quis ex semper, sit amet convallis ligula porttitor. Morbi a sapien vitae dolor lobortis efficitur.</p>
    <cite>Alex Marlow – A Lorem Ipsum Co.</cite>
  </div>
</section>

<footer class="site-footer">
  <h3 class="footer-heading" style="left:120px">Useful Links</h3>
  <ul class="abs link-col" style="left:120px">
    <li>Home</li><li>Online Image &amp; Reputation Management</li><li>Blog</li><li>Customer Retention &amp; Loyalty</li><li>Mobile Marketing</li>
  </ul>
  <ul class="abs link-col" style="left:388px">
    <li>OutBound Marketing</li><li>Support to Complete the Sale</li><li>Social Media Marketing</li><li>InBound Marketing</li>
  </ul>
  <div class="abs follow">Follow Us on :<i></i><i></i><i></i><i></i><i></i></div>

  <h3 class="footer-heading" style="left:710px">Latest Blog</h3>
  <div class="abs post" style="top:94px">
    <div class="date">Dec<b>03</b></div>
    <p>Maecenas purus neque, tincidunt sed urna a,<br>maximus semper nisi ut vel libero.</p>
    <a>read more</a>
  </div>
  <div class="abs post" style="top:208px">
    <div class="date">Dec<b>03</b></div>
    <p>Maecenas purus neque, tincidunt sed urna a,<br>maximus semper nisi ut vel libero.</p>
    <a>read more</a>
  </div>
  <div class="abs post" style="top:322px;border-bottom:none">
    <div class="date">Dec<b>03</b></div>
    <p>Maecenas purus neque, tincidunt sed urna a,<br>maximus semper nisi ut vel libero.</p>
    <a>read more</a>
  </div>
</footer>

<div class="abs footer-bottom" style="left:0;width:1200px">
  <div class="abs legal">Terms &nbsp;| &nbsp;Privacy Policy &nbsp;| &nbsp;Terms and Conditions &nbsp;| &nbsp;Sitemap</div>
  <div class="abs copyright">Copyright © 2015 QuillHarbor. All Rights Reserved</div>
</div>

</body>
</html>
```